Medical Internet Marketing Company Needs a Site!

We need a new, fresh website for our search engine optimization and social media marketing company. We specialize in helping medical practices, doctors, physicians, and hospitals with their online presence and web ranking. The site should lean towards being suited for these audiences.

We have several examples of website that we like as well as things that we like about them.

Here are sites that we enjoy.

www.brightwavelab.com

It's a good design for the site all around. The videos, buttons, and images are all excellent. They did a fine job.

- We really like their "contact us" side bar and want to include one like it on the secondary pages.

www.corvantis.net

- We don't like the "thickness" of the top navigation bar.
- We like the page colors, easy navigation, and big call to action phone number in the top right corner.

http://www.teluvo.com/

Out of all the examples provided, Teluvo is our favorite and closest look and style to what we are looking for.

- We really like the openness of the design, such as space between the text and background.

- We want a price page in a style very similar to their pricing page with the services listed and check-marks, etc. although we intend to have multiple service package columns much like Corvantis's SEO pricing page.

- The way the video fits into the home page header is very organized, simple, and attention grabbing. We intend to place a slider with videos here.

- We need a page design that will allow for an image slider like Teluvo's Features page.

Here's a great example of a medical internet marketing website: http://www.dermaplex.com/

Target Market(s)

Our target market is doctors, typically male and typically 40-45 years old. I

Industry/Entity Type

Marketing

Requirements
Must have
• The homepage should have a slider in the video. Interior pages should have a video in the very top similar to how they do it on www.brightwavelab.com

The top navigation tabs needed are:
- Home
- Solutions
- Resources
- About
- Why Quelvo
- Contact

The sidebar should have a GREAT call to action in it on interior pages.

There should be one interior page that is similar to this - http://www.teluvo.com/pricing/

There needs to be a page with multiple boxes that take up a row of the web page's body. This page will house all the case studies similar to brightwave lab's: http://www.brightwavelab.com/success-stories/case-studies/ The one exception is we want the case studies to be inside of "boxes" instead of between horizontal lines like brightwave lab's.
Nice to have
• Color, professional, and clean. GREAT use of calls to actions.

```html
<!DOCTYPE html>
<html lang="en">
<head>
<meta charset="utf-8">
<title>Quelvo – Internet Marketing Planning</title>
<link rel="stylesheet" href="https://fonts.googleapis.com/css2?family=PT+Sans:ital,wght@0,400;0,700;1,400&family=PT+Sans+Narrow:wght@400;700&family=Open+Sans:ital,wght@0,400;0,600;1,400&display=swap">
<style>
  :root {
    --ink: #3a3a3a;
    --muted: #6b6b6b;
    --header-top: #2b2b2b;
    --header-bottom: #050505;
    --gold: #f7c21f;
    --gold-deep: #f3a712;
    --hero-light: #fff3a8;
    --hero-mid: #ffd63b;
    --hero-deep: #f8b314;
    --orange: #f39a0c;
    --orange-deep: #ee8a05;
    --green: #8cc33a;
    --green-deep: #6fae25;
    --page: #ffffff;
    --line: #d8d8d8;
    --footer-ink: #1c1c1c;
  }
  * { box-sizing: border-box; margin: 0; padding: 0; }
  html, body { width: 800px; height: 1200px; overflow: hidden; background: var(--page); }
  body { font-family: "Open Sans", Arial, sans-serif; color: var(--ink); }
  .page { position: relative; width: 800px; height: 1200px; overflow: hidden; }

  /* Header */
  .site-header { position: absolute; inset: 0 0 auto 0; height: 80px;
    background: linear-gradient(var(--header-top), var(--header-bottom)); }
  .call-line { position: absolute; right: 92px; top: 5px; display: flex; align-items: center; gap: 8px;
    color: #fff; font: 700 13px "PT Sans", Arial, sans-serif; }
  .call-icon { width: 20px; height: 20px; background: #e8e8e8; border-radius: 3px; display: grid; place-items: center; }
  .brand { position: absolute; left: 94px; top: 40px; display: flex; align-items: center; gap: 10px;
    color: #e6e6e6; font: 400 30px "PT Sans", Arial, sans-serif; letter-spacing: 2px; line-height: 1; }
  .brand-mark { width: 26px; height: 20px; background: var(--gold); }
  .main-nav { position: absolute; right: 86px; top: 25px; display: flex; height: 58px; }
  .main-nav a { display: block; padding: 22px 11px 0; color: #eaeaea; text-decoration: none;
    font: 400 12px "PT Sans Narrow", Arial, sans-serif; }
  .main-nav a.is-current { background: linear-gradient(var(--gold), var(--gold-deep)); color: #2a2a2a; font-weight: 700;
    width: 42px; padding-left: 8px; padding-right: 8px; }

  /* Hero */
  .hero { position: absolute; left: 0; top: 80px; width: 800px; height: 273px; overflow: hidden;
    background: radial-gradient(ellipse at 30% 20%, var(--hero-light), var(--hero-mid) 55%, var(--hero-deep)); }
  .hero-swoosh { position: absolute; inset: 0; }
  .hero-copy { position: absolute; left: 94px; top: 28px; width: 270px; }
  .hero-title { font: 700 26px "PT Sans Narrow", Arial, sans-serif; color: #4a4a4a; }
  .hero-points { list-style: none; margin-top: 13px; }
  .hero-points li { font: 400 10.5px "Open Sans", Arial, sans-serif; color: #4a4a4a; line-height: 17px; padding-left: 8px; position: relative; }
  .hero-points li::before { content: ""; position: absolute; left: 0; top: 6px; border: 3px solid transparent; border-left: 4px solid #4a4a4a; }
  .hero-intro { margin-top: 10px; font-size: 9.5px; line-height: 12.5px; color: #8a6a12; }
  .signup-button { position: absolute; left: 94px; top: 221px; width: 150px; height: 35px; border-radius: 5px;
    background: linear-gradient(#f99b21, #ea6d07); box-shadow: 0 2px 3px rgba(0,0,0,.25);
    display: flex; align-items: center; gap: 8px; padding-left: 6px; color: #fff; text-decoration: none;
    font: 400 16px "PT Sans Narrow", Arial, sans-serif; }
  .signup-badge { width: 30px; height: 28px; border-radius: 4px; background: #2d9fe0; display: grid; place-items: center; }

  .monitor { position: absolute; left: 380px; top: 29px; }
  .monitor-screen { position: absolute; left: 14px; top: 12px; width: 299px; height: 175px;
    background: linear-gradient(120deg, #6ba7d9 0%, #d46ab0 35%, #f0a347 60%, #a24ad0 85%); }
  .video-controls { position: absolute; left: 14px; top: 172px; width: 299px; height: 15px; background: rgba(0,0,0,.45); }

  /* Welcome */
  .welcome { position: absolute; left: 94px; top: 400px; width: 350px; }
  .section-title { font: 400 21px "PT Sans", Arial, sans-serif; color: #3c3c3c; }
  .section-title strong { font-weight: 700; }
  .value-list { list-style: none; margin-top: 14px; }
  .value-list li { position: relative; padding-left: 22px; font-size: 8.6px; line-height: 16px; color: var(--muted); }
  .value-list li::before { content: ""; position: absolute; left: 0; top: 4px; width: 12px; height: 8px; background: var(--gold-deep); }
  .text-link { display: inline-block; margin-top: 10px; font-size: 9px; color: var(--muted); text-decoration: underline; }

  .testimonials { position: absolute; left: 481px; top: 400px; width: 226px; }
  .quote { margin-top: 14px; font: italic 400 8.4px/13.5px "Open Sans", Arial, sans-serif; color: #555; }
  .quote-author { margin-top: 12px; text-align: right; font-size: 8.2px; font-weight: 600; color: #333; }
  .quote + .quote-author + .quote { margin-top: 20px; padding-top: 14px; border-top: 1px solid var(--line); }

  /* Services */
  .services { position: absolute; left: 94px; top: 753px; width: 613px; }
  .service-grid { display: flex; justify-content: space-between; margin-top: 18px; }
  .service-card { width: 137px; }
  .service-name { font: 400 11.5px "PT Sans", Arial, sans-serif; color: #2e2e2e; text-transform: uppercase; letter-spacing: .2px; }
  .service-image { margin-top: 8px; height: 70px; border: 1px solid var(--line); box-shadow: 0 1px 2px rgba(0,0,0,.15); }
  .img-mobile { background: linear-gradient(135deg, #e9e9e9, #b9c7d8 50%, #5a5f66); }
  .img-education { background: linear-gradient(90deg, #4a3a3a, #c8a89a 45%, #6b2c3f); }
  .img-social { background: linear-gradient(135deg, #f3f3f3, #bcd8ee 50%, #e9f1f6); }
  .img-portal { background: linear-gradient(90deg, #eef2f3, #d7dfe2 55%, #a9b5bd); }
  .service-text { margin-top: 11px; font-size: 8.4px; line-height: 12.5px; color: #555; }
  .small-button { display: inline-block; margin-top: 8px; padding: 3px 11px; border: 1px solid #cfcfcf; border-radius: 2px;
    background: linear-gradient(#ffffff, #e6e6e6); font-size: 6.5px; color: #444; text-decoration: none; }

  /* Footer */
  .site-footer { position: absolute; left: 0; top: 955px; width: 800px; height: 245px; }
  .footer-shape { position: absolute; inset: 0; }
  .footer-col { position: absolute; top: 95px; width: 140px; }
  .footer-title { font: 400 13px "PT Sans", Arial, sans-serif; color: var(--footer-ink); }
  .footer-links { list-style: none; margin-top: 7px; }
  .footer-links li { font-size: 7.2px; line-height: 14px; color: #222; }
  .social-row { display: flex; gap: 5px; margin-top: 8px; }
  .social-dot { width: 21px; height: 21px; border-radius: 50%; background: #3a3a3a; box-shadow: inset 0 0 0 2px #5a5a5a; }
  .news-form { margin-top: 8px; width: 137px; }
  .news-field { height: 14px; background: #fff; margin-bottom: 6px; font-size: 6.5px; padding: 2px 4px; color: #333; }
  .news-message { height: 46px; }
  .subscribe-button { display: block; margin-left: auto; width: 54px; height: 16px; border-radius: 3px; background: linear-gradient(#3a3a3a, #111);
    color: #fff; font-size: 8px; text-align: center; line-height: 16px; }
  .copyright { position: absolute; left: 0; right: 0; bottom: 7px; text-align: center; font-size: 7.5px; font-weight: 600; color: #2a2a2a; }
</style>
</head>
<body>
<div class="page">

  <header class="site-header">
    <div class="call-line">
      <span class="call-icon">
        <svg width="12" height="12" viewBox="0 0 24 24"><path d="M6.6 10.8a15 15 0 0 0 6.6 6.6l2.2-2.2a1 1 0 0 1 1-.25 11.4 11.4 0 0 0 3.6.57 1 1 0 0 1 1 1V20a1 1 0 0 1-1 1A17 17 0 0 1 3 4a1 1 0 0 1 1-1h3.5a1 1 0 0 1 1 1c0 1.25.2 2.45.57 3.57a1 1 0 0 1-.25 1z" fill="#222"/></svg>
      </span>
      Call us on: 123-456-789
    </div>
    <div class="brand"><span class="brand-mark"></span>QUELVO</div>
    <nav class="main-nav">
      <a class="is-current" href="#">Home</a>
      <a href="#">Solutions</a>
      <a href="#">Resources</a>
      <a href="#">About</a>
      <a href="#">Why Quelvo</a>
      <a href="#">Contact</a>
    </nav>
  </header>

  <section class="hero">
    <svg class="hero-swoosh" width="800" height="273" viewBox="0 0 800 273">
      <path d="M0 190 C200 150 420 260 800 170 L800 273 L0 273 Z" fill="#f7a60f" opacity=".55"/>
      <path d="M0 225 C260 190 480 270 800 215 L800 273 L0 273 Z" fill="#f39a0c" opacity=".6"/>
      <path d="M0 160 C220 120 460 230 800 130" stroke="#fff6c0" stroke-width="2" fill="none" opacity=".7"/>
    </svg>
    <div class="hero-copy">
      <h1 class="hero-title">Internet Marketing Planning</h1>
      <ul class="hero-points">
        <li>Proven to help grow medical practices — 6,000+ satisfied clients</li>
        <li>Websites, mobile sites, local search and more...</li>
        <li>Fast, easy and affordable</li>
      </ul>
      <p class="hero-intro">QUELVO is a national, medical Internet-marketing group.Weempower doctors nationwide by building their practices with highly specialized engagement strategies designed to bring in real patients.</p>
    </div>
    <a class="signup-button" href="#">
      <span class="signup-badge"><svg width="18" height="16" viewBox="0 0 18 16"><path d="M9 16 L1 7 H6 V0 H12 V7 H17 Z" fill="#fff"/></svg></span>
      Sign up for free
    </a>
    <div class="monitor">
      <svg width="327" height="265" viewBox="0 0 327 265">
        <rect x="2" y="2" width="323" height="200" rx="8" fill="#1a1a1a" stroke="#8a8a8a" stroke-width="2"/>
        <rect x="2" y="202" width="323" height="20" fill="#d9d9d9"/>
        <path d="M130 222 L197 222 L205 252 L122 252 Z" fill="#cfcfcf"/>
        <ellipse cx="163" cy="254" rx="55" ry="5" fill="#b8b8b8"/>
      </svg>
      <div class="monitor-screen" role="img" aria-label="Video slide: colourful close-up photograph"></div>
      <svg style="position:absolute;left:130px;top:70px" width="56" height="56" viewBox="0 0 56 56"><circle cx="28" cy="28" r="26" fill="rgba(255,255,255,.25)"/><path d="M21 15 L42 28 L21 41 Z" fill="rgba(255,255,255,.85)"/></svg>
      <div class="video-controls"></div>
    </div>
  </section>

  <section class="welcome">
    <h2 class="section-title">Welcome to <strong>QUELVO</strong> Website</h2>
    <ul class="value-list">
      <li>We are a GROUP: dispels the possible perception of being a one-man show andconveys intimacy, specialization and collaboration (vs. company, agency or firm).</li>
      <li>We EMPOWER doctors nationwide: immediately describes core audience and sizeof market, plus, the word "empower" elevates QUELVO as the authority on medical Internet marketing vs. being perceived as a mere provider.</li>
      <li>We BUILD their practices: implies an immediate and specific benefit and purposeluses the word "build" to complement the QUELVO name.</li>
      <li>Highly specialized PATIENT-ENGAGEMENT strategies: Patient engagement is hugefor QUELVO – its "spine," if you will, that is supported by QUELVO'S results-focusedSEO and outstanding social media services.</li>
      <li>Designed to bring in REAL PATIENTS: This is QUELVO's key diferentiator.QUELVO knows that its medical clients aren't just satisfied with anyone visiting their medical websites. They want the right someone so their practice can be successful. Also note the wording "designed to" -- which promises intent but is not a guarantee. Just a safeguard.</li>
      <li>QUELVO is the medical industry's SEO specialist, unlike its "general practitioner" competitors.</li>
    </ul>
    <a class="text-link" href="#">Read more</a>
  </section>

  <aside class="testimonials">
    <h2 class="section-title">Client <strong>Testimonials</strong></h2>
    <p class="quote">"Placerat sit amet leo. Vestibulum rutrum risus vel enim tincidunt a sagittis velit vehicula. Vestibulum ante ipsum primis in faucibus orci luctus et ultrices posuere cubilia Curae.Quisque elementum venenatis libero."</p>
    <p class="quote-author">Daniel Marsh, CEO Northline Telecom</p>
    <p class="quote">"Placerat sit amet leo. Vestibulum rutrum risus vel enim tincidunt a sagittis velit vehicula. Vestibulum ante ipsum primis in faucibus orci luctus et ultrices posuere cubilia Curae.Quisque elementum venenatis libero.sagittis velit vehicula. Vestibulum ante ipsum primis in faucibus orci luctus et ultrices sagittis velit vehicula. Vestibulum ante ipsum primis in faucibus orci luctus et ultrices."</p>
    <p class="quote-author">Glen Porter, General Manager</p>
    <a class="text-link" href="#" style="margin-top:16px">More Testimonials</a>
  </aside>

  <section class="services">
    <h2 class="section-title">Medical Website <strong>Services</strong></h2>
    <div class="service-grid">
      <article class="service-card">
        <h3 class="service-name">Mobile Websites</h3>
        <div class="service-image img-mobile" role="img" aria-label="Smartphone with app icons"></div>
        <p class="service-text">Lorem Ipsum is simply dummy text of the printing and typesetting industry. Lorem Ipsum has been the industry's.</p>
        <a class="small-button" href="#">Read more</a>
      </article>
      <article class="service-card">
        <h3 class="service-name">Patients Education</h3>
        <div class="service-image img-education" role="img" aria-label="Doctor talking with a patient"></div>
        <p class="service-text">Lorem Ipsum is simply dummy text of the printing and typesetting industry. Lorem Ipsum has been the industry's.</p>
        <a class="small-button" href="#">Read more</a>
      </article>
      <article class="service-card">
        <h3 class="service-name">Social &amp; Media Blogs</h3>
        <div class="service-image img-social" role="img" aria-label="Network of connected social media nodes"></div>
        <p class="service-text">Lorem Ipsum is simply dummy text of the printing and typesetting industry. Lorem Ipsum has been the industry's.</p>
        <a class="small-button" href="#">Read more</a>
      </article>
      <article class="service-card">
        <h3 class="service-name">Doctor's Portal</h3>
        <div class="service-image img-portal" role="img" aria-label="Portrait of a doctor in a bright clinic"></div>
        <p class="service-text">Lorem Ipsum is simply dummy text of the printing and typesetting industry. Lorem Ipsum has been the industry's.</p>
        <a class="small-button" href="#">Read more</a>
      </article>
    </div>
  </section>

  <footer class="site-footer">
    <svg class="footer-shape" width="800" height="245" viewBox="0 0 800 245">
      <defs>
        <linearGradient id="footerOrange" x1="0" y1="0" x2="0" y2="1"><stop offset="0" stop-color="#f7a81a"/><stop offset="1" stop-color="#ef8c05"/></linearGradient>
        <linearGradient id="footerGreen" x1="0" y1="0" x2="1" y2="1"><stop offset="0" stop-color="#9ccd45"/><stop offset="1" stop-color="#6fae25"/></linearGradient>
      </defs>
      <path d="M0 0 C250 60 520 100 800 110 L800 245 L0 245 Z" fill="url(#footerOrange)"/>
      <path d="M800 5 C640 70 470 150 370 245 L800 245 Z" fill="url(#footerGreen)"/>
    </svg>
    <div class="footer-col" style="left:94px">
      <h4 class="footer-title">Main Links</h4>
      <ul class="footer-links"><li>Home</li><li>Solutions</li><li>Resources</li><li>About</li><li>Why Quelvo</li><li>Contact</li></ul>
    </div>
    <div class="footer-col" style="left:252px">
      <h4 class="footer-title">Follow us on</h4>
      <div class="social-row">
        <span class="social-dot" role="img" aria-label="Social profile link"></span>
        <span class="social-dot" role="img" aria-label="Social profile link"></span>
        <span class="social-dot" role="img" aria-label="Social profile link"></span>
        <span class="social-dot" role="img" aria-label="Social profile link"></span>
      </div>
    </div>
    <div class="footer-col" style="left:411px">
      <h4 class="footer-title">Other Links</h4>
      <ul class="footer-links"><li>Contact Us</li><li>Terms &amp; Conditions</li><li>Privacy Policy</li><li>Legal Disclosure</li><li>User Agreement</li></ul>
    </div>
    <div class="footer-col" style="left:569px">
      <h4 class="footer-title">Get News Updates</h4>
      <div class="news-form">
        <div class="news-field">Name:</div>
        <div class="news-field">Email:</div>
        <div class="news-field news-message">Message:</div>
        <span class="subscribe-button">Subscribe</span>
      </div>
    </div>
    <p class="copyright">© 2012 Quelvo Webiste.All Rights Reserved</p>
  </footer>

</div>
</body>
</html>
```